Images and design ideas provided: Postcard size flier

2 sided postcard size flier to hand people on the street.

A FUN tax business needs a postcard size flier to hand people on the street. Not a typical serious, quiet, office so make the image fun!

Exact wording, logo and key images provided. You are free to add other images as you see fit (such as money).

Side 1: Use image of lady looking up (she should be looking at text provided).All spanish and english text provided. Logo in bottom right corner. Address at bottom of card.

Side 2: Image of lady holding money and pointing. Remove money and have her holding a sign/or some other creative way to have her looking at text. All spanish and english text provided. Logo in bottom right corner. Address at bottom of card.

Size: 4" x 6" horizontal or vertical is ok
Each side can be different and image/design does not have to be related.

Target Market(s)

Age 18-35

Industry/Entity Type

Accounting

Font styles to use
Sans Serif

Colors

Designer to choose colors to be used in the design.

Requirements
Must have
• Use text document provided. All text goes on both sides.
• Should be easy to read from a few feet away.
Nice to have
• Bright colors to attract attention of people walking by to grab flier/card. Images of money ok.
Should not have
• No images of calculators or typical accounting tax forms.

```html
<!DOCTYPE html>
<html lang="en">
<head>
<meta charset="utf-8">
<title>Refund Royale – Postcard Flier</title>
<link rel="stylesheet" href="https://fonts.googleapis.com/css2?family=Arvo:ital,wght@0,700;1,700&family=Quicksand:wght@400;500;700&family=Roboto:ital,wght@0,400;1,400&family=Oswald:wght@600&display=swap">
<style>
  :root {
    --blue: #3a73bd;
    --blue-deep: #2f63a8;
    --red: #e52843;
    --paper: #efefef;
    --ink: #222222;
    --bar: #2b2b2b;
    --white: #ffffff;
    --page: #e4e1dc;
  }
  * { margin: 0; padding: 0; box-sizing: border-box; }
  html, body { width: 1200px; height: 1200px; overflow: hidden; background: var(--page); }
  .card {
    position: absolute; left: 195px; width: 810px; height: 540px;
    overflow: hidden; background: var(--paper);
    box-shadow: 0 6px 18px rgba(0,0,0,.18);
  }
  .card--front { top: 40px; }
  .card--back { top: 620px; }
  .card__shapes { position: absolute; inset: 0; }
  .headline {
    position: absolute; font-family: "Arvo", serif; font-weight: 700; white-space: nowrap; line-height: 1;
  }
  .headline .amount { color: var(--red); font-style: italic; }
  .subline { position: absolute; font-family: "Quicksand", sans-serif; font-weight: 500; white-space: nowrap; }
  .photo { position: absolute; }
  .contact {
    position: absolute; font-family: "Roboto", sans-serif; font-size: 16px; line-height: 20px;
  }
  .contact__row { display: flex; align-items: flex-start; gap: 10px; }
  .contact__row + .contact__row { margin-top: 12px; }
  .contact__phone { font-style: italic; font-size: 17px; letter-spacing: .5px; }
  .contact svg { flex: none; margin-top: 2px; }
  .divider { position: absolute; width: 1.5px; }
  .brand {
    position: absolute; font-family: "Quicksand", sans-serif; font-weight: 700;
    font-size: 30px; line-height: 1; white-space: nowrap; letter-spacing: .5px;
  }

  /* front */
  .card--front .headline--en { left: 36px; top: 28px; font-size: 64px; color: var(--white); }
  .card--front .subline--en { left: 37px; top: 108px; font-size: 31px; color: var(--white); }
  .card--front .headline--es { left: 378px; top: 212px; font-size: 47px; color: var(--blue); line-height: 58px; }
  .card--front .rule { position: absolute; left: 382px; top: 330px; width: 368px; height: 2px; background: var(--red); }
  .card--front .subline--es { left: 379px; top: 339px; font-size: 20px; color: var(--ink); white-space: normal; width: 400px; line-height: 26px; }
  .card--front .photo { left: 16px; top: 212px; width: 310px; height: 328px;
    background: linear-gradient(160deg, #d9b04a 0%, #b8a774 25%, #8f9a6a 55%, #7f8a5c 80%, #9b3a34 100%);
    border-radius: 120px 120px 0 0; }
  .card--front .contact { left: 263px; top: 443px; color: var(--white); }
  .card--front .divider { left: 507px; top: 446px; height: 60px; background: rgba(255,255,255,.55); }
  .card--front .brand { left: 540px; top: 463px; color: var(--red); }

  /* back */
  .card--back .headline--es { left: 0; width: 810px; text-align: center; top: 30px; font-size: 43px; color: var(--white); }
  .card--back .subline--es { left: 168px; top: 83px; font-size: 21px; color: var(--white); padding-bottom: 4px; border-bottom: 1px solid rgba(255,255,255,.7); }
  .card--back .headline--en { left: 252px; top: 200px; font-size: 52px; color: var(--blue); }
  .card--back .rule { position: absolute; left: 305px; top: 272px; width: 382px; height: 2px; background: var(--ink); }
  .card--back .subline--en { left: 306px; top: 290px; font-size: 33px; color: var(--ink); }
  .card--back .photo { left: 0; top: 215px; width: 250px; height: 325px;
    background: linear-gradient(165deg, #d8ae48 0%, #c0453c 22%, #9aa277 50%, #7d8a5d 80%, #6f7a52 100%);
    border-radius: 0 110px 0 0; }
  .offer {
    position: absolute; left: 136px; top: 228px; width: 112px; height: 112px; border-radius: 50%;
    background: #3a3a3a; border: 6px solid var(--red);
    display: flex; flex-direction: column; align-items: center; justify-content: center;
    font-family: "Oswald", sans-serif; font-weight: 600; line-height: 1; font-size: 23px;
  }
  .offer__top { color: var(--white); }
  .offer__bottom { color: var(--red); }
  .card--back .contact { left: 238px; top: 446px; color: var(--white); }
  .card--back .divider { left: 508px; top: 446px; height: 56px; background: rgba(255,255,255,.8); }
  .card--back .brand { left: 540px; top: 460px; color: var(--white); }
</style>
</head>
<body>

<section class="card card--front">
  <svg class="card__shapes" width="810" height="540" viewBox="0 0 810 540" aria-hidden="true">
    <rect width="810" height="540" fill="var(--paper)"/>
    <path d="M0 0H810V202C740 168 630 140 500 146C340 156 170 208 0 198Z" fill="var(--red)"/>
    <path d="M0 0H810V176C740 148 630 126 500 132C340 140 170 184 0 166Z" fill="var(--blue)"/>
    <rect y="430" width="810" height="93" fill="var(--bar)"/>
    <rect y="523" width="810" height="17" fill="var(--blue)"/>
  </svg>

  <h1 class="headline headline--en">Get <span class="amount">$100</span> Cash Now!</h1>
  <p class="subline subline--en">With Paid Tax Preparation</p>

  <h2 class="headline headline--es">Reciba <span class="amount">$100</span> en<br>efectivo ahora!</h2>
  <div class="rule"></div>
  <p class="subline subline--es">con la preparacion pagada de sus impuestos</p>

  <div class="photo" role="img" aria-label="Photo of a cheerful woman in a gold crown hat and green royal robe, arms raised, looking up at the text"></div>

  <address class="contact">
    <div class="contact__row">
      <svg width="16" height="20" viewBox="0 0 16 20"><path d="M8 0C3.6 0 0 3.4 0 7.6 0 13 8 20 8 20s8-7 8-12.4C16 3.4 12.4 0 8 0Zm0 10.5A3 3 0 1 1 8 4.5a3 3 0 0 1 0 6Z" fill="var(--red)"/></svg>
      <span>418 Harlow Ave. Bronx<br>NY 10452</span>
    </div>
    <div class="contact__row">
      <svg width="18" height="18" viewBox="0 0 24 24"><path d="M6.6 10.8a15.2 15.2 0 0 0 6.6 6.6l2.2-2.2c.3-.3.7-.4 1-.2 1.1.4 2.3.6 3.6.6.6 0 1 .4 1 1V20c0 .6-.4 1-1 1A17 17 0 0 1 3 4c0-.6.4-1 1-1h3.5c.6 0 1 .4 1 1 0 1.3.2 2.5.6 3.6.1.3 0 .7-.2 1Z" fill="var(--red)"/></svg>
      <span class="contact__phone">(718) 555-0147</span>
    </div>
  </address>
  <div class="divider"></div>
  <div class="brand">Refund Royale</div>
</section>

<section class="card card--back">
  <svg class="card__shapes" width="810" height="540" viewBox="0 0 810 540" aria-hidden="true">
    <rect width="810" height="540" fill="var(--paper)"/>
    <path d="M0 0H810V86C640 120 480 146 380 146C230 146 100 118 0 104Z" fill="var(--red)"/>
    <path d="M0 0H810V78C640 112 480 138 380 138C230 138 100 110 0 96Z" fill="var(--blue)"/>
    <path d="M0 392C150 410 300 420 420 418C590 414 720 384 810 358V540H0Z" fill="var(--blue)"/>
    <path d="M0 400C150 418 300 428 420 426C590 422 720 392 810 366V540H0Z" fill="var(--red)"/>
  </svg>

  <h2 class="headline headline--es">Reciba <span class="amount">$100</span> en efectivo ahora!</h2>
  <p class="subline subline--es">con la preparacion pagada de sus impuestos</p>

  <h1 class="headline headline--en">Get <span class="amount">$100</span> Cash Now!</h1>
  <div class="rule"></div>
  <p class="subline subline--en">With Paid Tax Preparation</p>

  <div class="photo" role="img" aria-label="Photo of a smiling woman in a gold crown hat and green royal robe, pointing at the offer sign and the text"></div>
  <div class="offer"><span class="offer__top">SPECIAL</span><span class="offer__bottom">OFFER</span></div>

  <address class="contact">
    <div class="contact__row">
      <svg width="16" height="20" viewBox="0 0 16 20"><path d="M8 0C3.6 0 0 3.4 0 7.6 0 13 8 20 8 20s8-7 8-12.4C16 3.4 12.4 0 8 0Zm0 10.5A3 3 0 1 1 8 4.5a3 3 0 0 1 0 6Z" fill="var(--white)"/></svg>
      <span>418 Harlow Ave. Bronx<br>NY 10452</span>
    </div>
    <div class="contact__row">
      <svg width="18" height="18" viewBox="0 0 24 24"><path d="M6.6 10.8a15.2 15.2 0 0 0 6.6 6.6l2.2-2.2c.3-.3.7-.4 1-.2 1.1.4 2.3.6 3.6.6.6 0 1 .4 1 1V20c0 .6-.4 1-1 1A17 17 0 0 1 3 4c0-.6.4-1 1-1h3.5c.6 0 1 .4 1 1 0 1.3.2 2.5.6 3.6.1.3 0 .7-.2 1Z" fill="var(--white)"/></svg>
      <span class="contact__phone">(718) 555-0147</span>
    </div>
  </address>
  <div class="divider"></div>
  <div class="brand">Refund Royale</div>
</section>

</body>
</html>
```